International Company needs a Letterhead & Envelope Design

Our Company name is Corvale Brightwick Limited.
We'd like to ask the Designers for the luxurious and sophisticated design. Our logo is very simple and neat with letter logos, so we look forward to more professional and refined designs from Designers.
We look forward to providing you with a great design.
Thanks very much in advance.

```html
<!DOCTYPE html>
<html lang="en">
<head>
<meta charset="utf-8">
<title>Corvale Brightwick Limited – Letterhead &amp; Envelope</title>
<link href="https://fonts.googleapis.com/css2?family=Mulish:wght@400;700;800&display=swap" rel="stylesheet">
<style>
  :root {
    --backdrop: #939598;
    --paper: #ffffff;
    --band: #231f20;
    --brand-grey: #58585a;
    --text: #3c3c3e;
  }
  * { margin: 0; padding: 0; box-sizing: border-box; }
  html, body {
    width: 1200px; height: 828px; overflow: hidden;
    background: var(--backdrop);
    font-family: "Mulish", Arial, sans-serif;
    color: var(--text);
  }
  .stationery { position: relative; width: 1200px; height: 828px; }
  .sheet {
    position: absolute;
    background: var(--paper);
    box-shadow: 0 1px 3px rgba(0,0,0,0.25);
  }
  .band { position: absolute; display: block; }
  .wordmark {
    position: absolute;
    font-weight: 800;
    font-size: 22px;
    letter-spacing: 0.5px;
    line-height: 1;
    color: var(--brand-grey);
    white-space: nowrap;
  }

  /* Letterhead */
  .letterhead { left: 21px; top: 21px; width: 556px; height: 786px; }
  .letterhead .band-top { left: 0; top: 0; }
  .letterhead .band-bottom { right: 0; bottom: 0; }
  .letterhead .wordmark { left: 41px; top: 45px; }
  .contact {
    position: absolute; left: 408px; top: 41px;
    font-size: 7.6px; line-height: 10.4px;
  }
  .web-address {
    position: absolute; right: 41px; top: 755px;
    font-size: 10px; font-weight: 700; letter-spacing: 0.2px;
  }

  /* Envelope */
  .envelope { left: 598px; top: 270px; width: 582px; height: 290px; }
  .envelope .band-top { left: 0; top: 0; }
  .envelope .wordmark { left: 13px; top: 35px; }
  .return-address {
    position: absolute; left: 13px; top: 63px;
    font-size: 7.6px; line-height: 10px;
  }
</style>
</head>
<body>
<main class="stationery">

  <section class="sheet letterhead" aria-label="Letterhead">
    <svg class="band band-top" width="330" height="14" viewBox="0 0 330 14" aria-hidden="true">
      <polygon points="0,0 328,0 315,14 0,14" fill="var(--band)"/>
    </svg>
    <div class="wordmark">CORVALE BRIGHTWICK</div>
    <address class="contact" style="font-style:normal">
      48 Harlow Ave. Austin, TX 78701<br>
      555.014.2290<br>
      info@CorvaleBrightwick.com
    </address>
    <div class="web-address">www.CORVALEBRIGHTWICK.com</div>
    <svg class="band band-bottom" width="328" height="13" viewBox="0 0 328 13" aria-hidden="true">
      <polygon points="14,0 328,0 328,13 0,13" fill="var(--band)"/>
    </svg>
  </section>

  <section class="sheet envelope" aria-label="Envelope">
    <svg class="band band-top" width="330" height="14" viewBox="0 0 330 14" aria-hidden="true">
      <polygon points="0,0 328,0 315,14 0,14" fill="var(--band)"/>
    </svg>
    <div class="wordmark">CORVALE BRIGHTWICK</div>
    <address class="return-address" style="font-style:normal">48 Harlow Ave. Austin, TX 78701</address>
  </section>

</main>
</body>
</html>
```